Website Design for CloudKeel As a Service

We are building a service to allow customers to own their own private clouds easily and cheaply. Owning your own private cloud saves costs, and offers more flexibility than a public cloud provider but has historically been a complex and expensive option.

We plan to offer a service where we build and maintain your own private cloud on your own hardware for a cheap monthly costs. Similar to this service - https://stackorra.com/solutions/private-cloud

We already have a logo and branding in place - we'd like a website design to be tailored from this branding, see attached logo design.

Feel free to add important elements on the home page such as testimonials, client/partner logos, contact form, social media, etc using placeholder contents in addition to the document we attached.

We also plan to add sub-pages in the future so please make sure that your website design has a full navigation menu.

An example of the site we like: https://www.verimoxa.com/ we'd be happy for you to take inspiration from this website.

Target Market(s)

B2B focused, we are targeting start-up/small/medium sized companies who needs help with their cloud and IT infrastructure.

Industry/Entity Type

IT

Number of Pages Required

1 page

Font styles to use
Other font styles liked:
• Please refer to the attachment - font must have Mayeka Demi Bold & Retroica

Requirements
Must have
• Please add placeholder menu since we're planning to have subpages later on.

```html
<!DOCTYPE html>
<html lang="en">
<head>
<meta charset="utf-8">
<title>CloudKeel — Private Cloud as a Service</title>
<link href="https://fonts.googleapis.com/css2?family=Comfortaa:wght@500;700&family=Lato:wght@400;700&display=swap" rel="stylesheet">
<style>
:root{
  --blue:#1f74c8;
  --blue-dark:#135aa3;
  --blue-light:#cfe3f6;
  --navy:#0b1b33;
  --ink:#1b1f24;
  --text:#3a3f46;
  --grey-bg:#f1f3f6;
  --white:#ffffff;
  --footer:#0a0d12;
  --line:#d6dbe1;
}
*{box-sizing:border-box;margin:0;padding:0}
html,body{width:1200px;height:4101px;overflow:hidden}
body{font-family:'Lato',sans-serif;color:var(--text);background:var(--white);position:relative}
.display{font-family:'Comfortaa',sans-serif;font-weight:700}
section,header,footer{position:absolute;left:0;width:1200px}
.center{text-align:center;left:0;width:1200px}

/* header */
.site-header{top:0;height:70px;background:var(--white);border-top:3px solid var(--blue);box-shadow:0 1px 4px rgba(0,0,0,.08);z-index:5}
.brand{display:flex;align-items:center;gap:8px;font-family:'Comfortaa',sans-serif;font-weight:700;color:var(--blue);font-size:24px}
.brand-dot{width:22px;height:22px;border-radius:50%;background:var(--blue)}
.site-header .brand{position:absolute;left:132px;top:19px}
.main-nav{position:absolute;left:462px;top:24px;display:flex;gap:24px;font-size:12px;font-weight:700;color:var(--ink);letter-spacing:.2px}
.main-nav .active{color:var(--blue);border-bottom:1px solid var(--blue)}

/* hero */
.hero{top:70px;height:580px;overflow:hidden}
.hero-bg{position:absolute;inset:0;background:radial-gradient(ellipse at 50% 35%,#3d6a97 0%,#1a3a62 30%,#0d1f3a 65%,#08142a 100%)}
.hero-fade{position:absolute;left:0;bottom:0;width:1200px;height:120px;background:linear-gradient(180deg,rgba(255,255,255,0) 0%,rgba(255,255,255,.55) 55%,#fff 100%)}
.hero h1{position:absolute;top:170px;font-size:36px;line-height:41px;color:var(--white);font-weight:700}
.hero .lede{position:absolute;top:266px;left:300px;width:600px;font-size:14px;line-height:25px;color:#e6edf6;text-align:center}
.hero .ask{position:absolute;top:328px;font-size:15px;color:var(--white)}
.btn{display:inline-block;border-radius:20px;font-family:'Comfortaa',sans-serif;font-weight:700;font-size:14px;text-align:center}
.btn-solid{background:var(--blue);color:var(--white)}
.btn-outline{border:2px solid var(--blue);color:var(--blue)}
.btn-ghost{border:2px solid var(--white);color:var(--white)}
.hero .btn{position:absolute;left:525px;top:380px;width:150px;height:36px;line-height:36px}

/* section heading mark */
.mark{position:absolute;width:22px;height:22px;border-radius:50%;background:var(--blue);left:589px}
.sec-title{position:absolute;font-size:31px;color:var(--ink)}

/* benefits */
.benefits{top:650px;height:518px}
.benefit{position:absolute;top:172px;width:245px;height:305px;text-align:center;padding-top:40px}
.benefit.is-active{background:var(--white);border:1px solid #e3e6ea;border-radius:8px;box-shadow:0 2px 12px rgba(0,0,0,.12)}
.benefit .icon{width:100px;height:100px;border-radius:50%;background:var(--blue);margin:0 auto;position:relative;box-shadow:-14px -10px 0 6px var(--blue-light)}
.benefit .icon svg{position:absolute;left:25px;top:25px}
.benefit h3{font-size:15px;color:var(--ink);font-weight:400;margin-top:26px;letter-spacing:.3px}
.benefit .rule{width:26px;height:3px;background:var(--blue);margin:9px auto 12px}
.benefit p{font-size:12.5px;line-height:25px;width:200px;margin:0 auto}
.arrow{position:absolute;top:320px}

/* transformation */
.transform{top:1168px;height:712px;background:var(--grey-bg)}
.transform .body{position:absolute;top:182px;left:190px;width:820px;text-align:center;font-size:13px;line-height:28px;color:var(--ink)}
.transform .accent{position:absolute;top:272px;font-size:13px;line-height:25px;color:var(--blue)}
.trait{position:absolute;top:362px;width:194px;height:194px;border-radius:50%;background:var(--blue);color:var(--white);text-align:center;font-family:'Comfortaa',sans-serif;font-weight:700;font-size:16px;box-shadow:0 0 0 3px var(--white)}
.trait svg{display:block;margin:28px auto 8px}
.transform .btn{position:absolute;left:525px;top:598px;width:152px;height:40px;line-height:36px}

/* public cloud */
.public{top:1880px;height:760px;overflow:hidden}
.public-bg{position:absolute;inset:0;background:linear-gradient(160deg,#2a7fd0 0%,#1c6dbf 50%,#175fae 100%)}
.public .mark{background:var(--white);top:86px}
.public .sec-title{color:var(--white);top:120px}
.case{position:absolute;top:185px;width:302px;height:405px}
.case .photo{position:absolute;left:0;top:0;width:302px;height:222px}
.case .box{position:absolute;left:16px;top:188px;width:270px;height:217px;background:var(--white);text-align:center;padding-top:18px}
.case.is-active .box{border:2px solid var(--blue-dark)}
.case h3{font-family:'Comfortaa',sans-serif;font-weight:700;font-size:15px;line-height:27px;color:var(--ink)}
.case .rule{width:26px;height:3px;background:var(--blue);margin:8px auto 10px}
.case p{font-size:12.5px;line-height:28px;width:240px;margin:0 auto}
.public .btn{position:absolute;left:524px;top:640px;width:152px;height:40px;line-height:36px}

/* difference */
.difference{top:2640px;height:594px}
.diff-art{position:absolute;left:90px;top:125px;width:465px;height:345px;border-radius:120px 140px 60px 140px;background:radial-gradient(ellipse at 55% 45%,#2c7ccc 0%,#1a5fa8 55%,#124a88 100%)}
.difference .mark{left:615px;top:102px}
.difference .sec-title{left:615px;top:140px}
.diff-list{position:absolute;left:615px;top:200px;width:500px;list-style:none;font-size:13px;line-height:28px;color:var(--ink)}
.diff-list li{position:relative;padding-left:24px}
.diff-list li::before{content:"";position:absolute;left:0;top:9px;width:13px;height:9px;border-radius:5px 5px 2px 2px;background:var(--blue)}

/* contact */
.contact{top:3234px;height:576px;background:var(--grey-bg)}
.field{position:absolute;border:1px solid #8c95a1;border-radius:20px;background:var(--white);font-size:11px;color:#555;padding:10px 24px}
.contact .submit{position:absolute;left:138px;top:444px;width:153px;height:40px;line-height:40px;border-radius:20px;background:var(--blue);color:var(--white);font-size:15px;text-align:center;letter-spacing:.5px}
.divider{position:absolute;left:700px;top:204px;width:1px;height:322px;background:#9aa3ad}
.info{position:absolute;left:740px;display:flex;align-items:center;gap:20px;font-family:'Comfortaa',sans-serif;font-weight:700;font-size:15px;line-height:26px;color:var(--ink)}
.info .dot{width:54px;height:54px;border-radius:50%;background:var(--white);box-shadow:0 2px 8px rgba(0,0,0,.1);display:flex;align-items:center;justify-content:center;flex:none}
.info.phone{color:var(--blue);font-size:19px}

/* footer */
.site-footer{top:3810px;height:291px;background:var(--footer);color:var(--white)}
.site-footer .brand{position:absolute;left:0;width:1200px;top:90px;justify-content:center;color:var(--white);font-size:40px}
.site-footer .brand-dot{width:34px;height:34px;background:var(--white)}
.foot-nav{position:absolute;left:0;width:1200px;top:178px;display:flex;justify-content:center;gap:24px;font-size:13px;font-weight:700}
.copy{position:absolute;left:0;width:1200px;top:218px;text-align:center;font-size:10px;font-family:'Comfortaa',sans-serif;font-weight:700}
</style>
</head>
<body>

<header class="site-header">
  <div class="brand"><span class="brand-dot"></span>CloudKeel</div>
  <nav class="main-nav">
    <span class="active">HOME</span><span>ABOUT</span><span>BENEFITS</span><span>DIGITAL TRANSFORMATION</span><span>PUBLIC CLOUD</span><span>CONTACT US</span>
  </nav>
</header>

<section class="hero">
  <div class="hero-bg" role="img" aria-label="Dark blue network of glowing cloud and data lines"></div>
  <div class="hero-fade" role="img" aria-label="Soft white clouds along the lower edge"></div>
  <h1 class="display center">A groundbreaking way for your small business<br>to benefit from the power of the cloud</h1>
  <p class="lede">CloudKeel as a Service is here to help small businesses utilise the power of the cloud without complicated set-ups or scary price tags.</p>
  <p class="ask display center">Ready to modernise your infrastructure with a fully managed private cloud solution from CKaaS?</p>
  <span class="btn btn-solid">Contact us</span>
</section>

<section class="benefits" id="benefits">
  <div class="mark" style="top:72px"></div>
  <h2 class="sec-title display center" style="top:108px">How CKAAS Benefits Your Business</h2>
  <svg class="arrow" style="left:50px" width="36" height="16" viewBox="0 0 36 16"><path d="M35 8H2M9 1L2 8l7 7" fill="none" stroke="#1b1f24" stroke-width="2"/></svg>
  <svg class="arrow" style="left:1114px" width="36" height="16" viewBox="0 0 36 16"><path d="M1 8h33M27 1l7 7-7 7" fill="none" stroke="#1b1f24" stroke-width="2"/></svg>

  <div class="benefit" style="left:98px">
    <div class="icon"><svg width="50" height="50" viewBox="0 0 50 50" fill="none" stroke="#fff" stroke-width="2.5"><path d="M25 48V20M25 20l-10-10M25 20l10-10M10 6v8h8M40 6v8h-8"/></svg></div>
    <h3>TOTALLY FLEXIBLE</h3><div class="rule"></div>
    <p>Get the cloud you want and the latest innovations you need.</p>
  </div>
  <div class="benefit is-active" style="left:348px">
    <div class="icon"><svg width="50" height="50" viewBox="0 0 50 50" fill="none" stroke="#fff" stroke-width="2.5"><circle cx="25" cy="26" r="17"/><path d="M25 15v11l7 5M20 5h10"/></svg></div>
    <h3>FASTER</h3><div class="rule"></div>
    <p>Our private cloud solutions outpace public clouds</p>
  </div>
  <div class="benefit" style="left:600px">
    <div class="icon"><svg width="50" height="50" viewBox="0 0 50 50" fill="none" stroke="#fff" stroke-width="2.5"><circle cx="30" cy="24" r="14"/><path d="M30 16v16M26 20h6a3 3 0 010 6h-4a3 3 0 000 6h6"/><rect x="6" y="30" width="12" height="16"/></svg></div>
    <h3>GREATER VALUE FOR MONEY</h3><div class="rule"></div>
    <p>Totally transparent pricing for no nasty month-end surprises.</p>
  </div>
  <div class="benefit" style="left:852px">
    <div class="icon"><svg width="50" height="50" viewBox="0 0 50 50" fill="none" stroke="#fff" stroke-width="2.5"><rect x="9" y="5" width="26" height="36" rx="2"/><path d="M15 14h14M15 21h14M15 28h8"/><circle cx="36" cy="36" r="9"/></svg></div>
    <h3>NO CONSULTANCY FEES</h3><div class="rule"></div>
    <p>We'll work with you and charge set fees for everything.</p>
  </div>
</section>

<section class="transform" id="digital-transformation">
  <div class="mark" style="top:92px"></div>
  <h2 class="sec-title display center" style="top:128px">CKAAS Can Drive Your Digital Transformation Today</h2>
  <p class="body">Organisations of all shapes and sizes are reaping the time and money saving benefits that the cloud brings.<br>But for small businesses seeking to transition, managing the time and financial costs of transitioning, and knowing whether to opt for a public or private cloud can cause you to hit the pause button.</p>
  <p class="accent display center">CKAAS is here to help you switch on your cloud transformation in a way that works best for you<br>We deliver and support fully managed private cloud solutions that are:</p>

  <div class="trait" style="left:218px"><svg width="70" height="70" viewBox="0 0 70 70" fill="none" stroke="#fff" stroke-width="3"><circle cx="38" cy="38" r="24"/><path d="M38 24v14l9 6M30 6h16M38 6v8M4 34h12M6 42h10M8 50h10"/></svg>Fast</div>
  <div class="trait" style="left:409px"><svg width="70" height="70" viewBox="0 0 70 70" fill="none" stroke="#fff" stroke-width="3"><path d="M22 64V34l8-24 6 2-4 18h16a6 6 0 016 6l-4 22a8 8 0 01-8 6z"/></svg>Easy</div>
  <div class="trait" style="left:598px"><svg width="70" height="70" viewBox="0 0 70 70" fill="none" stroke="#fff" stroke-width="3"><rect x="18" y="28" width="34" height="26" rx="8"/><path d="M24 54v12h22V54M35 4v12M14 10l6 8M56 10l-6 8"/></svg>Powerful</div>
  <div class="trait" style="left:786px"><svg width="70" height="70" viewBox="0 0 70 70" fill="none" stroke="#fff" stroke-width="3"><rect x="6" y="40" width="24" height="24"/><path d="M14 30V6h50v50H40" stroke-dasharray="6 5"/><path d="M38 32l18-18M44 14h12v12"/></svg>Scalable</div>

  <span class="btn btn-outline">Get Started</span>
</section>

<section class="public" id="public-cloud">
  <div class="public-bg" role="img" aria-label="Blue technology background with server lights"></div>
  <div class="mark"></div>
  <h2 class="sec-title display center">If You're Using a Public Cloud Now</h2>

  <div class="case" style="left:129px">
    <div class="photo" role="img" aria-label="Hands typing on a laptop surrounded by floating data icons" style="background:linear-gradient(135deg,#1a2230,#6b4a3a 55%,#2f8fd9)"></div>
    <div class="box"><h3>You could be paying<br>too much</h3><div class="rule"></div>
      <p>Public cloud pricing structures have a habit of sneakily scaling up very quickly. With CKAAS, you'll always know what you're paying for your private cloud.</p></div>
  </div>
  <div class="case is-active" style="left:449px">
    <div class="photo" role="img" aria-label="Person at a laptop with a glowing cloud connected to service icons" style="background:linear-gradient(135deg,#3a3f46,#7a5a44 50%,#1e2a38)"></div>
    <div class="box"><h3>You're likely not getting the<br>benefits of full functionality</h3><div class="rule"></div>
      <p>Public cloud providers cannot adopt new innovations and functions as quickly and easily as the private cloud solutions you'll get from CKAAS.</p></div>
  </div>
  <div class="case" style="left:768px">
    <div class="photo" role="img" aria-label="Glowing blue cloud over a circuit board" style="background:radial-gradient(ellipse at 50% 50%,#5fb3ff,#1b4fa0 50%,#0b1c45)"></div>
    <div class="box"><h3>You'll be tied to the services<br>your provider can provide</h3><div class="rule"></div>
      <p>Public cloud providers will have a limited suite of products and services to offer you. A CKAAS private cloud has no such limitations.</p></div>
  </div>

  <span class="btn btn-ghost">Let's talk</span>
</section>

<section class="difference" id="about">
  <div class="diff-art" role="img" aria-label="Blue illustration of a hand holding a cloud with data streams"></div>
  <div class="mark"></div>
  <h2 class="sec-title display">The CKAAS Difference</h2>
  <ul class="diff-list">
    <li>We'll quickly get to grips with what your organisation needs, and deliver it via our private cloud solutions.</li>
    <li>Enjoy the ease of the public cloud, combined with the features, innovations and flexibility of the private cloud.</li>
    <li>You can focus on your core business while we support you with a dedicated cloud infrastructure.</li>
    <li>We'll create and deliver the launchpad that will take your business forward.</li>
    <li>Get the benefits of your own cloud infrastructure and reduce your operational costs</li>
    <li>Fast and easy computing, storage and network resources</li>
    <li>Managed operations from private OpenLattice clouds and Kubernova</li>
    <li>We'll support your growth and scale your cloud as you need it.</li>
  </ul>
</section>

<section class="contact" id="contact">
  <div class="mark" style="top:98px"></div>
  <h2 class="sec-title display center" style="top:134px">Contact Us</h2>
  <div class="field" style="left:138px;top:216px;width:256px;height:40px">Full Name</div>
  <div class="field" style="left:402px;top:216px;width:256px;height:40px">Email Address</div>
  <div class="field" style="left:138px;top:266px;width:520px;height:40px">Phone Number</div>
  <div class="field" style="left:138px;top:316px;width:520px;height:110px">Message</div>
  <div class="submit">SUBMIT</div>
  <div class="divider"></div>
  <div class="info" style="top:233px"><span class="dot"><svg width="14" height="18" viewBox="0 0 14 18"><path d="M7 0a7 7 0 017 7c0 5-7 11-7 11S0 12 0 7a7 7 0 017-7z" fill="#1f74c8"/><circle cx="7" cy="7" r="2.5" fill="#fff"/></svg></span>123 Lorem ipsum dolor sit amet<br>consectetur adipiscing</div>
  <div class="info phone" style="top:322px"><span class="dot"><svg width="16" height="16" viewBox="0 0 16 16"><path d="M3 0l3 4-2 2a10 10 0 006 6l2-2 4 3-2 3C7 16 0 9 0 3z" fill="#1f74c8"/></svg></span>+1 555 010 0199</div>
  <div class="info" style="top:404px"><span class="dot"><svg width="16" height="12" viewBox="0 0 16 12"><rect width="16" height="12" rx="1" fill="#1f74c8"/><path d="M1 1l7 6 7-6" fill="none" stroke="#fff" stroke-width="1.5"/></svg></span>info@cloudkeel.example</div>
</section>

<footer class="site-footer">
  <div class="brand"><span class="brand-dot"></span>CloudKeel</div>
  <nav class="foot-nav"><span>HOME</span><span>ABOUT</span><span>BENEFITS</span><span>DIGITAL TRANSFORMATION</span><span>PUBLIC CLOUD</span><span>CONTACT US</span></nav>
  <p class="copy">© copyrights 2022 CKAAS &nbsp; | &nbsp; All rights reserved.</p>
</footer>

</body>
</html>
```